Business Card for Makeup Artist

I need a business card designed for my makeup and hair artistry business which is primarily events and weddings focused. The card needs to be sleek, simple, stylish and appealing to women. I would prefer a white background but open to suggestions also. I also love the marble background look. I have attached some example pics. It needs to be a double sided card with logo and/or design on one side and contact details in the centre of the card on the other side. NO LOGO ON BACK. Examples attached.

Target Market(s)

Females age 14-55

Industry/Entity Type

Business

Contact Information for Business Card

Nora Vint
Principal Makeup Artist
P: 0413 925 214
E: nora@lumirabeauty.com.au
W: www.lumirabeauty.com.au

Requirements
Should not have
• No yellow, green, red or blue in the design.

```html
<!DOCTYPE html>
<html lang="en">
<head>
<meta charset="utf-8">
<title>Lumira – Business Card</title>
<link href="https://fonts.googleapis.com/css2?family=Questrial&family=Exo+2:wght@600&display=swap" rel="stylesheet">
<style>
  :root {
    --backdrop: #3a3a3c;
    --card-black: #1e1e1f;
    --card-grey: #55555a;
    --white: #ffffff;
    --pink: #d96aab;
    --ink: #2a1a24;
    --line-black: #0d0d0d;
  }
  * { box-sizing: border-box; margin: 0; padding: 0; }
  html, body {
    width: 1200px; height: 900px; overflow: hidden;
    background: var(--backdrop);
  }
  .canvas { position: relative; width: 1200px; height: 900px; }
  .card {
    position: absolute; width: 600px; height: 343px;
    border-radius: 22px; overflow: hidden;
    box-shadow: 0 14px 30px rgba(0,0,0,0.45);
  }
  .card-front { left: 140px; top: 90px; }
  .front-pattern {
    position: absolute; inset: 0;
    background: linear-gradient(152deg, var(--card-grey) 0%, var(--card-black) 45%, var(--card-black) 70%, var(--card-grey) 100%);
  }
  .front-brand {
    position: absolute; inset: 0;
    display: flex; flex-direction: column; align-items: center; justify-content: center;
  }
  .brand-name {
    font-family: "Questrial", sans-serif;
    font-size: 84px; color: var(--white);
    letter-spacing: 2px; line-height: 1;
  }
  .brand-tagline {
    margin-top: 10px;
    font-family: "Questrial", sans-serif;
    font-size: 24px; color: var(--white);
    letter-spacing: 3px;
  }
  .card-back { left: 460px; top: 467px; background: var(--white); }
  .card-back .wave { position: absolute; inset: 0; width: 100%; height: 100%; }
  .contact {
    position: absolute; left: 0; right: 0; top: 220px;
    text-align: center; color: var(--ink);
    font-family: "Questrial", sans-serif;
  }
  .contact-name {
    font-family: "Exo 2", sans-serif; font-weight: 600;
    font-size: 25px; line-height: 30px; color: var(--white); letter-spacing: 1.5px;
  }
  .contact-title { font-size: 14px; line-height: 18px; }
  .contact-list { list-style: none; margin-top: 6px; font-size: 13.5px; line-height: 18px; }
  .contact-list span { margin-right: 8px; }
</style>
</head>
<body>
<main class="canvas">
  <section class="card card-front">
    <div class="front-pattern" role="img" aria-label="Diagonal grey and black stripe pattern"></div>
    <div class="front-brand">
      <div class="brand-name">Lumira</div>
      <div class="brand-tagline">MAKEUP ARTIST</div>
    </div>
  </section>

  <section class="card card-back">
    <svg class="wave" viewBox="0 0 600 343" preserveAspectRatio="none" aria-hidden="true">
      <path d="M0 150 C150 142 200 184 300 184 C420 184 520 152 600 122 L600 343 L0 343 Z" fill="var(--pink)" opacity="0.55"/>
      <path d="M0 158 C150 150 200 192 300 192 C420 192 520 160 600 132 L600 343 L0 343 Z" fill="var(--white)"/>
      <path d="M0 162 C150 154 200 196 300 196 C420 196 520 164 600 137 L600 343 L0 343 Z" fill="var(--line-black)"/>
      <path d="M0 174 C150 166 200 208 300 208 C420 208 520 176 600 150 L600 343 L0 343 Z" fill="var(--pink)"/>
    </svg>
    <div class="contact">
      <div class="contact-name">NORA VINT</div>
      <div class="contact-title">Principal Makeup Artist</div>
      <ul class="contact-list">
        <li><span>P:</span>0413 925 214</li>
        <li><span>E:</span>nora@lumirabeauty.com.au</li>
        <li><span>W:</span>www.lumirabeauty.com.au</li>
      </ul>
    </div>
  </section>
</main>
</body>
</html>
```